Audio-Visual & Video Communications Business Requires a Cutting-edge Business Card Design

LinkHarbor is a new Audio-Visual & Video Communications company in Cape Town, South Africa that is looking for a cutting-edge business card design. We sell these products to the Corporate, Education & Hospitality markets and will also host an Online Shop for companies and individuals to purchase our products online.

We are already using the following two colours in our logo and draft website. Please incorporate these colours into the design. Please note that our website is still in the design stage if you need to visit it. Green #a0ce4e & Dark Grey #333333.
Updates

Hi,

Please note that I have uploaded our logo in an .eps format.

Target Market(s)

Corporate Companies, Education Institutions & Hospitality Markets

Industry/Entity Type

Business

Requirements
Nice to have
• It would be great if you could incorporate the services that we offer.

1. Consultation & Design
2. Project Management
3. Supply & Installation
4. Onsite Support Personal
5. Online Shop

```html
<!DOCTYPE html>
<html lang="en">
<head>
<meta charset="utf-8">
<title>LinkHarbor – Business Card</title>
<link rel="stylesheet" href="https://fonts.googleapis.com/css2?family=Arimo:wght@400&family=Open+Sans:ital,wght@0,400;0,700;1,400&display=swap">
<style>
  :root {
    --green: #6cb21f;
    --charcoal: #4a4a4a;
    --ink: #444444;
    --paper: #ffffff;
    --page: #ffffff;
  }
  * { margin: 0; padding: 0; box-sizing: border-box; }
  html, body { width: 1200px; height: 900px; overflow: hidden; background: var(--page); }
  .canvas { position: relative; width: 1200px; height: 900px; }

  .card {
    position: absolute;
    left: 372px;
    width: 468px;
    height: 287px;
    border-radius: 18px;
    overflow: hidden;
    background: var(--paper);
    box-shadow: 0 14px 26px rgba(0,0,0,0.22);
    font-family: "Arimo", Arial, sans-serif;
  }
  .card--front { top: 125px; }
  .card--back { top: 497px; }

  /* Front */
  .front-band {
    position: absolute; left: 0; top: 0; width: 100%; height: 97px;
    background: var(--charcoal);
  }
  .holder-name {
    position: absolute; left: 23px; top: 40px;
    font-family: "Open Sans", Arial, sans-serif; font-style: italic;
    font-size: 21px; color: var(--green);
  }
  .holder-email {
    position: absolute; right: 22px; top: 46px;
    font-size: 14px; color: var(--green);
  }
  .brand {
    position: absolute;
    display: flex; flex-direction: column; align-items: center;
    font-family: "Open Sans", Arial, sans-serif; font-weight: 700;
    color: var(--charcoal); letter-spacing: -0.3px;
  }
  .brand-dot { border-radius: 50%; background: var(--green); }
  .brand--front { left: 28px; top: 132px; width: 192px; }
  .brand--front .brand-dot { width: 62px; height: 62px; margin-bottom: 12px; }
  .brand--front .brand-name { font-size: 24px; line-height: 1; }
  .website {
    position: absolute; left: 28px; top: 256px;
    font-size: 16px; color: var(--ink);
  }
  .divider {
    position: absolute; left: 270px; top: 172px; width: 3px; height: 115px;
    background: var(--green);
  }
  .address {
    position: absolute; left: 286px; top: 171px;
    font-size: 13px; line-height: 15px; color: var(--ink);
  }
  .phones {
    position: absolute; left: 285px; top: 243px;
    list-style: none; font-size: 13px; line-height: 15px; color: var(--ink);
  }
  .phones li { display: flex; align-items: center; gap: 5px; }
  .phones svg { width: 11px; height: 11px; fill: var(--ink); }

  /* Back */
  .brand--back { left: 0; top: 30px; width: 100%; }
  .brand--back .brand-dot { width: 66px; height: 66px; margin-bottom: 14px; }
  .brand--back .brand-name { font-size: 24px; line-height: 1; }
  .back-band {
    position: absolute; left: 0; top: 144px; width: 100%; height: 143px;
    background: var(--charcoal);
  }
  .services {
    position: absolute; left: 136px; top: 24px; width: 196px;
    list-style: none; text-align: center;
    font-family: "Open Sans", Arial, sans-serif; font-weight: 700;
    font-size: 12px; color: var(--paper);
  }
  .services li { height: 21.5px; line-height: 19px; border-bottom: 2px solid var(--green); }
  .services li:last-child { border-bottom: none; }
</style>
</head>
<body>
<main class="canvas">
  <section class="card card--front">
    <div class="front-band">
      <p class="holder-name">Daniel Marsh</p>
      <p class="holder-email">me@linkharbor.co.za</p>
    </div>
    <div class="brand brand--front">
      <span class="brand-dot"></span>
      <span class="brand-name">LinkHarbor</span>
    </div>
    <p class="website">www.linkharbor.co.za</p>
    <span class="divider"></span>
    <address class="address" style="font-style:normal">42 Keswick Road<br>Cape Town - South Africa</address>
    <ul class="phones">
      <li><svg viewBox="0 0 12 12" aria-hidden="true"><path d="M3 0h6v12H3zM4 1v6h4V1z"/></svg>+27 21 555-0182</li>
      <li><svg viewBox="0 0 12 12" aria-hidden="true"><path d="M0 4q6-4 12 0v2H9V4.5H3V6H0zM2 7h8l1 4H1z"/></svg>+27 21 555-0147</li>
    </ul>
  </section>

  <section class="card card--back">
    <div class="brand brand--back">
      <span class="brand-dot"></span>
      <span class="brand-name">LinkHarbor</span>
    </div>
    <div class="back-band">
      <ul class="services">
        <li>Consultation &amp; Design</li>
        <li>Project Management</li>
        <li>Supply &amp; Installation</li>
        <li>Onsite Support Personal</li>
        <li>Online Shop</li>
      </ul>
    </div>
  </section>
</main>
</body>
</html>
```